Poster for a an ad on Facebook and website

Event is a hot rod..cool car cruise across Southern Ontario on September 21st and 22nd see www.lakeshoremotorparade7.com ad is to catch people's eyes and make them want to join in the Cruise. Two examples are included as ideas..folks travel from the PHOTOBOOTH's in Fort Erie and St.Thomas where they have had thier phots taken..small car gatherings break out at stops all along the 225km route..

Target Market(s)

car enthusiasts

Industry/Entity Type

automotive ..hot rods collector cars

Requirements
Must have
• Dates and a cool look--KTR presents sponsor logo as attached
Nice to have
• incorporate Hwy#3..thats the route

```html
<!DOCTYPE html>
<html lang="en">
<head>
<meta charset="utf-8">
<title>Ontario's Lakeshore Motor Parade</title>
<link rel="stylesheet" href="https://fonts.googleapis.com/css2?family=Bebas+Neue&family=Fredoka:wght@600&family=Oswald:wght@500;700&family=Shrikhand&display=swap">
<style>
  :root {
    --red: #b31b1e;
    --orange: #f5a623;
    --cream: #fdfbe8;
    --yellow: #f9b81b;
    --navy: #25306b;
    --ink: #1a1a1a;
    --white: #ffffff;
    --pale: #fbe27a;
  }
  * { margin: 0; padding: 0; box-sizing: border-box; }
  html, body { width: 948px; height: 1200px; overflow: hidden; background: var(--red); }
  .poster { position: relative; width: 948px; height: 1200px; background: var(--red); }
  .panel {
    position: absolute; left: 35px; top: 47px; width: 878px; height: 1112px;
    background: var(--cream); border: 7px solid var(--orange); border-radius: 14px;
  }
  .sponsor {
    position: absolute; font-family: "Oswald", sans-serif; font-weight: 700;
    color: var(--navy); line-height: 1;
  }
  .sponsor-main { left: 108px; top: 100px; font-size: 52px; letter-spacing: 2px; }
  .sponsor-partner { left: 690px; top: 92px; font-size: 26px; text-transform: uppercase; letter-spacing: 1px; }
  .presents {
    position: absolute; left: 0; width: 948px; top: 174px; text-align: center;
    font-family: "Oswald", sans-serif; font-weight: 500; font-size: 22px; color: var(--ink);
  }
  .arch {
    position: absolute; left: 120px; top: 196px; width: 709px; height: 898px;
    background: var(--yellow); border: 3px solid var(--ink);
    border-radius: 354px 354px 26px 26px;
  }
  .date-badge { position: absolute; left: 722px; top: 158px; width: 172px; height: 172px; }
  .date-text {
    position: absolute; left: 722px; top: 206px; width: 172px; text-align: center;
    font-family: "Oswald", sans-serif; font-weight: 500; font-size: 22px; line-height: 1.3;
    color: var(--white); transform: rotate(12deg);
  }
  .title-kicker {
    position: absolute; left: 0; width: 948px; top: 246px; text-align: center;
    font-family: "Shrikhand", cursive; font-size: 36px; color: var(--pale);
    -webkit-text-stroke: 1.5px var(--ink); transform: rotate(-3deg);
  }
  .title-main {
    position: absolute; left: 0; width: 948px; top: 300px; text-align: center;
    font-family: "Shrikhand", cursive; font-size: 80px; color: var(--red);
    -webkit-text-stroke: 2px var(--ink); text-shadow: 5px 5px 0 var(--ink);
    transform: rotate(-3deg);
  }
  .route {
    position: absolute; left: 380px; top: 452px; width: 200px; text-align: center;
    font-family: "Fredoka", sans-serif; font-weight: 600; color: var(--white);
    line-height: 1; transform: rotate(-4deg);
  }
  .route-stop { font-size: 26px; display: block; }
  .route-join { font-size: 15px; display: block; margin: 2px 0; }
  .car {
    position: absolute; left: 187px; top: 552px; width: 590px; height: 355px;
    background: linear-gradient(160deg, #f2f2f2 0%, #bdbdbd 50%, #3a3a3a 100%);
    border: 4px solid var(--ink); border-radius: 60px 120px 40px 40px;
  }
  .camera {
    position: absolute; left: 183px; top: 856px; width: 126px; height: 150px;
    background: linear-gradient(180deg, #e8e8ea 0 28%, var(--navy) 28% 55%, #2a2a2a 55% 100%);
    border-radius: 8px;
  }
  .photobooth-pill {
    position: absolute; left: 300px; top: 930px; width: 461px; height: 74px;
    border: 3px solid var(--red); border-radius: 37px; display: flex;
    align-items: center; justify-content: center;
    font-family: "Shrikhand", cursive; font-size: 29px; color: var(--red);
  }
  .tagline {
    position: absolute; left: 120px; width: 709px; top: 1030px; text-align: center;
    font-family: "Bebas Neue", sans-serif; font-size: 45px; letter-spacing: 1px; color: var(--navy);
  }
  .web {
    position: absolute; left: 0; width: 948px; top: 1118px; text-align: center;
    font-family: "Oswald", sans-serif; font-weight: 500; font-size: 22px;
    letter-spacing: 4px; color: var(--navy); text-transform: uppercase;
  }
</style>
</head>
<body>
<main class="poster">
  <div class="panel"></div>

  <div class="sponsor sponsor-main">KTR</div>
  <div class="sponsor sponsor-partner">Halcyon Parts</div>
  <p class="presents">PRESENTS</p>

  <div class="arch"></div>

  <svg class="date-badge" viewBox="0 0 172 172" aria-hidden="true">
    <polygon fill="var(--navy)" points="86,4 97,16 111,8 117,23 133,21 133,37 149,40 143,55 157,63 147,76 158,88 145,97 152,112 136,116 137,132 121,131 116,147 101,142 92,157 80,147 67,158 60,144 44,149 41,133 25,132 28,116 13,109 23,96 12,84 25,75 17,61 32,55 28,39 44,38 46,22 62,26 70,12 82,20"/>
  </svg>
  <p class="date-text">SEPTEMBER<br>21-22, 2024</p>

  <h1>
    <span class="title-kicker">Ontario's Lakeshore</span>
    <span class="title-main">Motor Parade</span>
  </h1>

  <p class="route">
    <span class="route-stop">FORT ERIE</span>
    <span class="route-join">to</span>
    <span class="route-stop">ST.THOMAS</span>
  </p>

  <div class="car" role="img" aria-label="Black and white photo of a 1950s classic hardtop car"></div>
  <div class="camera" role="img" aria-label="Vintage camera with flash"></div>
  <div class="photobooth-pill">Visit Our Photobooth!</div>

  <p class="tagline">WHERE CLASSICS MEET THE OPEN ROAD</p>
  <p class="web">www.lakeshoremotorparade7.com</p>
</main>
</body>
</html>
```